Investigation Tool App - Static Vornex Ad Image

We need a static image design that promotes our website, which provides an online incident investigation collaboration tool. I would like this static image for Vornex, but I am also seeking the same design in a Taskaro Ad ratio.

We would like to see engaging ad graphics that capture the essence of collaboration, time saving, fast "impact-to-learnings" type vibe. As it helps them collaborate and facilitate the investigation on our interactive canvas and then it has an automated report builder that is AI-assisted to turn their information into coherent sentences in the report, it is not fully AI generated (this is important as i feel people inherently distrust AI generated content).

This tool is aimed at safety professionals in mining, construction and oil & gas who want an easy way to facilitate investigations virtually or in person without having to use whiteboards and double handle information and that want to be able to generate a report and learnings on the same day to quickly prevent further harm.

I have included a bunch of snips of my site and features etc - please feel free to use any of them but dont be constrained by these.

Target Market(s)

Safety Professionals/ Managers in Mining, Oil & Gas & Construction

Industry/Entity Type

Mining, Oil & Gas & Construction

Font styles to use
Sans Serif

Requirements
Nice to have
• Modern, pain point focussed, visual of investigation map and or nodes
Should not have
• No em-dashes, no gimmicky language or terms

```html
<!DOCTYPE html>
<html lang="en">
<head>
<meta charset="utf-8">
<title>Still Using Whiteboards For Investigations?</title>
<link href="https://fonts.googleapis.com/css2?family=Poppins:wght@300;400;600;800;900&family=Inter:wght@400;600;700&display=swap" rel="stylesheet">
<style>
  :root{
    --brand-blue:#2766e8;
    --white:#ffffff;
    --ink:#111111;
    --muted:#6b7280;
    --line:#d5d8de;
    --page:#ffffff;
    --photo-a:#e9ebee;
    --photo-b:#c9ced6;
    --photo-c:#9fb3cc;
    --tag-blue:#cfe0fb;
    --tag-green:#c9efd3;
    --tag-orange:#fbc9a6;
    --tag-yellow:#fbe7a1;
    --tag-purple:#ddd0fb;
    --tag-grey:#dde1e6;
  }
  *{box-sizing:border-box;margin:0;padding:0}
  html,body{width:1200px;height:1200px;overflow:hidden;background:var(--page)}
  .ad{position:relative;width:1200px;height:1200px;overflow:hidden;font-family:"Poppins",Arial,sans-serif}

  .hero{position:absolute;left:0;top:0;width:1200px;height:400px;background:var(--brand-blue);color:var(--white);text-align:center}
  .hero-title{position:absolute;top:62px;left:0;width:100%;font-weight:800;font-size:66px;line-height:70px;letter-spacing:1px}
  .hero-lead{position:absolute;top:222px;left:0;width:100%;font-weight:300;font-size:39px;letter-spacing:.5px}
  .hero-sub{position:absolute;top:282px;left:0;width:100%;font-weight:400;font-size:28px;line-height:40px}

  .photo{position:absolute;left:0;top:400px;width:1200px;height:397px;
    background:linear-gradient(90deg,var(--photo-b) 0%,var(--photo-c) 25%,var(--photo-a) 38%,#f4f5f6 70%,var(--photo-b) 100%)}

  .versus{position:absolute;left:524px;top:721px;width:128px;height:128px;border-radius:50%;background:var(--brand-blue);
    color:var(--white);font-weight:900;font-style:italic;font-size:58px;display:flex;align-items:center;justify-content:center;z-index:3;letter-spacing:-2px}

  .app{position:absolute;left:0;top:797px;width:1200px;height:403px;background:#f3f4f6;font-family:"Inter",Arial,sans-serif}
  .app-window{position:absolute;left:14px;top:14px;width:1136px;height:389px;background:var(--white)}
  .app-header{position:absolute;left:0;top:0;width:100%;height:50px;border-bottom:1px solid var(--line)}
  .brand{position:absolute;left:56px;top:14px;font-family:"Poppins",Arial,sans-serif;font-weight:800;font-size:22px;color:var(--ink)}
  .module{position:absolute;left:178px;top:20px;font-weight:700;font-size:12px;letter-spacing:1.5px;color:var(--brand-blue)}
  .doc-name{position:absolute;right:24px;top:19px;font-weight:700;font-size:13px;color:var(--ink)}
  .scrollbar{position:absolute;right:0;top:0;width:12px;height:100%;background:#eef0f2}
  .scrollbar::after{content:"";position:absolute;left:3px;top:14px;width:6px;height:300px;border-radius:3px;background:#a3a8b0}
  .outside{position:absolute;right:0;top:0;width:36px;height:100%;background:
    linear-gradient(#e8eaed 1px,transparent 1px) 0 0/12px 12px,linear-gradient(90deg,#e8eaed 1px,transparent 1px) 0 0/12px 12px,#f9fafb}

  .map{position:absolute;left:148px;top:102px;width:974px;height:320px;border:1px solid var(--line);border-radius:3px;background:var(--white)}

  .group{position:absolute;border:1px solid #9aa0a8;border-radius:6px;background:var(--white)}
  .group-name{position:absolute;left:6px;top:-7px;background:var(--white);border:1px solid #9aa0a8;border-radius:3px;padding:0 4px;font-size:6px;line-height:10px;color:#333}

  .card{position:absolute;background:var(--white);border-radius:3px;box-shadow:0 1px 4px rgba(0,0,0,.22);font-size:6.5px;line-height:8px;color:#222;text-align:center;overflow:hidden}
  .card-label{display:block;font-size:5px;line-height:8px;letter-spacing:.6px;font-weight:600;color:#445}
  .card-text{display:block;padding:4px 5px}
  .card-date{display:block;background:var(--ink);color:var(--white);font-size:5.5px;line-height:9px}
  .card-tag{display:block;font-size:5.5px;line-height:9px;color:#333}
  .is-sequence .card-label{background:var(--tag-blue)}
  .is-control .card-label{background:var(--tag-green)}
  .is-control .card-tag{background:var(--tag-green)}
  .is-evidence .card-label{background:var(--tag-grey)}
  .is-evidence .card-tag{color:var(--muted)}
  .is-risk .card-label{background:var(--tag-orange)}
  .is-risk .card-tag{background:#fde0e0}
  .is-factor-a .card-label{background:var(--tag-yellow)}
  .is-factor-b .card-label{background:var(--tag-green)}
  .is-factor-c .card-label{background:var(--tag-purple)}

  .person{position:absolute;width:80px;text-align:center;font-size:6px;line-height:8px;color:#222}
  .person svg{display:block;margin:0 auto 4px}
</style>
</head>
<body>
<main class="ad">

  <section class="hero">
    <h1 class="hero-title">STILL USING WHITEBOARDS<br>FOR INVESTIGATIONS?</h1>
    <p class="hero-lead">MOVE YOUR INCIDENT INVESTIGATIONS ONLINE.</p>
    <p class="hero-sub">Collaborate in real-time, capture insights once, and generate<br>reports instantly.</p>
  </section>

  <div class="photo" role="img" aria-label="Photo of a safety professional in a denim jacket writing on a ruled whiteboard grid in an office"></div>

  <div class="versus">VS</div>

  <section class="app">
    <div class="app-window">
      <header class="app-header">
        <span class="brand">Corvane</span>
        <span class="module">SYSTEM MAP</span>
        <span class="doc-name">Document Name: Test Investigation</span>
      </header>
      <div class="outside"></div>
      <div class="scrollbar" style="right:36px"></div>
    </div>

    <div class="map" style="left:100px;top:103px;width:970px;height:310px"></div>

    <!-- Incident sequence -->
    <div class="group" style="left:178px;top:157px;width:588px;height:88px">
      <span class="group-name">Incident Sequence</span>
    </div>
    <div class="card is-sequence" style="left:200px;top:170px;width:92px"><span class="card-label">SEQUENCE STEP</span><span class="card-text">Supervisor stops at work area</span><span class="card-date">10 Mar 10:15</span></div>
    <div class="card is-sequence" style="left:314px;top:170px;width:92px"><span class="card-label">SEQUENCE STEP</span><span class="card-text">Light vehicle parked near pit</span><span class="card-date">10 Mar 10:18</span></div>
    <div class="card is-sequence" style="left:428px;top:170px;width:92px"><span class="card-label">SEQUENCE STEP</span><span class="card-text">Truck operator starts reversing</span><span class="card-date">10 Mar 10:21</span></div>
    <div class="card is-sequence" style="left:542px;top:170px;width:92px"><span class="card-label">SEQUENCE STEP</span><span class="card-text">Truck moves toward parked vehicle</span><span class="card-date">10 Mar 10:22</span></div>
    <div class="card is-sequence" style="left:656px;top:170px;width:92px"><span class="card-label">SEQUENCE STEP</span><span class="card-text">Operator stops and calls emergency</span><span class="card-date">10 Mar 10:24</span></div>

    <!-- Involved people -->
    <div class="group" style="left:182px;top:250px;width:172px;height:170px">
      <span class="group-name">Involved People</span>
    </div>
    <div class="person" style="left:188px;top:272px">
      <svg width="38" height="38" viewBox="0 0 38 38"><circle cx="19" cy="19" r="19" fill="#1f1f1f"/><circle cx="19" cy="19" r="15" fill="#fff"/><circle cx="19" cy="15" r="5" fill="#1f1f1f"/><path d="M10 29a9 7 0 0 1 18 0z" fill="#1f1f1f"/></svg>Haul Truck Operator</div>
    <div class="person" style="left:270px;top:272px">
      <svg width="38" height="38" viewBox="0 0 38 38"><circle cx="19" cy="19" r="19" fill="#1f1f1f"/><circle cx="19" cy="19" r="15" fill="#fff"/><circle cx="19" cy="15" r="5" fill="#1f1f1f"/><path d="M10 29a9 7 0 0 1 18 0z" fill="#1f1f1f"/></svg>Light Vehicle Driver</div>
    <div class="person" style="left:188px;top:338px">
      <svg width="38" height="38" viewBox="0 0 38 38"><circle cx="19" cy="19" r="19" fill="#1f1f1f"/><circle cx="19" cy="19" r="15" fill="#fff"/><circle cx="19" cy="15" r="5" fill="#1f1f1f"/><path d="M10 29a9 7 0 0 1 18 0z" fill="#1f1f1f"/></svg>Site Supervisor</div>
    <div class="person" style="left:270px;top:338px">
      <svg width="38" height="38" viewBox="0 0 38 38"><circle cx="19" cy="19" r="19" fill="#1f1f1f"/><circle cx="19" cy="19" r="15" fill="#fff"/><circle cx="19" cy="15" r="5" fill="#1f1f1f"/><path d="M10 29a9 7 0 0 1 18 0z" fill="#1f1f1f"/></svg>Mine Inspector</div>

    <!-- Risk -->
    <div class="group" style="left:373px;top:250px;width:101px;height:170px">
      <span class="group-name">Risk</span>
    </div>
    <div class="card is-risk" style="left:382px;top:270px;width:84px"><span class="card-label">CONDITION</span><span class="card-text">Truck entered zone without clearance</span><span class="card-tag">Material</span></div>
    <div class="card is-risk" style="left:382px;top:345px;width:84px"><span class="card-label">CONDITION</span><span class="card-text">Vehicle parked in blind spot</span><span class="card-tag">Material</span></div>

    <!-- Identified factors -->
    <div class="group" style="left:492px;top:250px;width:275px;height:170px">
      <span class="group-name">Identified Factors</span>
    </div>
    <div class="card is-factor-a" style="left:503px;top:270px;width:78px"><span class="card-label">FACTOR</span><span class="card-text">Loader placed inside haul path</span></div>
    <div class="card is-factor-a" style="left:590px;top:270px;width:78px"><span class="card-label">FACTOR</span><span class="card-text">Operator used wrong signal</span></div>
    <div class="card is-factor-b" style="left:677px;top:270px;width:78px"><span class="card-label">FACTOR</span><span class="card-text">No spotter was present</span></div>
    <div class="card is-factor-c" style="left:503px;top:340px;width:78px"><span class="card-label">FACTOR</span><span class="card-text">Site rules not clear</span></div>
    <div class="card is-factor-c" style="left:590px;top:340px;width:78px"><span class="card-label">FACTOR</span><span class="card-text">Work plan skipped radio check</span></div>
    <div class="card is-factor-c" style="left:677px;top:340px;width:78px"><span class="card-label">FACTOR</span><span class="card-text">Inspection timing not set</span></div>

    <!-- Controls -->
    <div class="group" style="left:785px;top:157px;width:99px;height:263px">
      <span class="group-name">Controls &amp; Barriers</span>
    </div>
    <div class="card is-control" style="left:793px;top:172px;width:82px"><span class="card-label">CONTROL</span><span class="card-text">Exclusion zone not maintained</span><span class="card-tag">Procedure</span></div>
    <div class="card is-control" style="left:793px;top:258px;width:82px"><span class="card-label">CONTROL</span><span class="card-text">No clear radio call made</span><span class="card-tag">Admin</span></div>
    <div class="card is-control" style="left:793px;top:336px;width:82px"><span class="card-label">CONTROL</span><span class="card-text">Spotter not assigned to area</span><span class="card-tag">Missing</span></div>

    <!-- Evidence -->
    <div class="group" style="left:901px;top:157px;width:102px;height:263px">
      <span class="group-name">Evidence</span>
    </div>
    <div class="card is-evidence" style="left:911px;top:172px;width:82px"><span class="card-label">EVIDENCE</span><span class="card-text">Dashcam footage of reversing truck</span><span class="card-tag">Video</span></div>
    <div class="card is-evidence" style="left:911px;top:258px;width:82px"><span class="card-label">EVIDENCE</span><span class="card-text">Photos taken after the event</span><span class="card-tag">Photo</span></div>
    <div class="card is-evidence" style="left:911px;top:336px;width:82px"><span class="card-label">EVIDENCE</span><span class="card-text">Statement from truck operator</span><span class="card-tag">Statement</span></div>
  </section>

</main>
</body>
</html>
```